Charting True North institute for nonprofits needs brochure

The Charting True North performance management institute helps nonprofits clarify the intended impact of their programs on clients. What does a nonprofit want to accomplish - and what does it need to measure so that it can tell if they've achieved impact? The Institute is about to recruit participanting organizations. We have a lot of wording on a 2 page "flyer" that describes the institute...but it is a very ugly piece that looks unprofessional. We are looking for designs that are consistent with the KTV Advisory Group look (see our website). We are aware that we may have too much wording.

Target Market(s)

Nonprofit organization Executive Directors

Industry/Entity Type

Non-Profit

Font styles to use
Sans Serif

Requirements
Must have
• Must be able to be emailed to a client and printed on 8.5x11 paper. Doesn't matter to me if that makes it a tri-fold or two-fold.
• Need to be able to drop in later the actual dates of the program.
• Go to our website to see how we present ourselves. www.ktvadvisory.example
Nice to have
• See our website for KTV Advisory's "look". Our colors are green and gray (in the logo), with complementary colors of blue and orange.
• Looking for creativity in the graphics design. Our two page document has way too many words. The word impact is very important to the concept of performance management (and I'm not sure it's in the 2 page write up) - so you could do something with that word if you wanted to.
• Could use Mabel's pic if it makes sense.
Should not have
• No new logo for the Charting True North institute. It should be clear that KTV Advisory Group is the entity that offers the institute.

```html
<!DOCTYPE html>
<html lang="en">
<head>
<meta charset="utf-8">
<title>Charting True North – Performance Management Institute</title>
<link href="https://fonts.googleapis.com/css2?family=Nunito+Sans:wght@300;400;700;800&display=swap" rel="stylesheet">
<style>
:root{
  --green:#8dc63f;
  --gray:#808285;
  --gray-dark:#6d6e71;
  --text:#58595b;
  --paper:#ffffff;
  --backdrop:#eeeeee;
}
*{box-sizing:border-box;margin:0;padding:0}
html,body{width:1200px;height:1200px;overflow:hidden;background:var(--backdrop)}
body{font-family:"Nunito Sans",Arial,sans-serif;color:var(--text);position:relative}
.spread{position:absolute;left:20px;top:153px;width:1300px;height:1002px;transform:scale(.8923);transform-origin:0 0;background:var(--paper);box-shadow:0 6px 20px rgba(0,0,0,.18)}
.abs{position:absolute}
.page-left{left:0;top:0;width:650px;height:970px;background:linear-gradient(90deg,#fff 85%,#f0f0f0 100%)}
.footer-band{left:0;top:970px;width:1300px;height:32px;background:var(--gray)}
.title{left:0;top:44px;width:650px;text-align:center;font-size:22px;line-height:24px;font-weight:400;color:#333}
.title-rule{left:250px;top:109px;width:150px;height:2px;background:var(--green)}
.copy{font-size:14.4px;line-height:16.2px;font-weight:300;text-align:justify}
.copy p{margin-bottom:16px}
.copy ul{list-style:none}
.copy li{position:relative;padding-left:29px}
.copy li::before{content:"•";position:absolute;left:0}
.col-a{left:47px;top:136px;width:267px}
.col-b{left:337px;top:136px;width:266px}
.schedule{left:47px;top:541px;width:556px;border-collapse:collapse;font-size:11.2px;font-weight:400;color:#333}
.schedule caption{background:var(--green);color:#fff;font-size:15px;height:22px;line-height:22px}
.schedule th{background:var(--gray);color:#fff;font-weight:400;height:22px;font-size:11.5px;border-left:1px solid #fff}
.schedule th:first-child{border-left:0}
.schedule td{height:33px;border-bottom:1px solid #444;line-height:13px;padding:0 7px}
.schedule td.when,.schedule td.where{text-align:center}
.footnote{left:47px;top:893px;font-size:11.2px;color:#333}
.deliverables{left:650px;top:47px;width:398px;height:189px;background:var(--gray);color:#fff;padding:22px 25px 0 46px;font-size:14.4px;line-height:18px;font-weight:300}
.deliverables h2{font-size:14.5px;font-weight:800;margin-bottom:1px}
.deliverables ul{list-style:none}
.deliverables li{position:relative;padding-left:16px}
.deliverables li::before{content:"•";position:absolute;left:0}
.cost{left:1048px;top:47px;width:252px;height:189px;background:var(--green);color:#fff;text-align:center;padding-top:48px;font-size:15.5px;line-height:17px;font-weight:300}
.cost h2{font-size:20px;font-weight:800;line-height:20px}
.bio-a{left:697px;top:283px;width:266px}
.bio-b{left:986px;top:283px;width:267px}
.comments{left:650px;top:636px;width:650px;height:334px;background:var(--green);color:#fff;padding:46px 47px 0 47px;font-size:14.4px;line-height:17px;font-weight:300}
.comments h2{font-size:14.5px;font-weight:800;margin-bottom:14px}
.comments p{margin-bottom:15px}
</style>
</head>
<body>
<div class="spread">
  <div class="abs page-left"></div>

  <h1 class="abs title">Charting True North:<br>Performance Management Institute</h1>
  <div class="abs title-rule"></div>

  <div class="abs copy col-a">
    <p>KTV Advisory Group is pleased to present Charting True North, a performance management institute that combines individual technical assistance with cohort learning to strengthen an agency’s performance management system.</p>
    <p style="margin-bottom:0">What is Performance Management and why should nonprofits improve their performance management system?</p>
    <ul>
      <li>High performance within nonprofits is necessary because outcomes matter – to service consumers, staff, Board members, funders, and the community.</li>
      <li>Performance management is a process that provides agencies with the ability to manage to outcomes. Managing to outcomes is NOT a knee-jerk reaction to funder requirements but, instead, is mission-driven and provides a way to</li>
    </ul>
  </div>

  <div class="abs copy col-b">
    <p style="margin-bottom:0;padding-left:29px">demonstrate the impact of the agency’s service delivery model.</p>
    <ul style="margin-bottom:16px">
      <li>Managing to outcomes supports sound strategic decision-making, planning, and business development.</li>
    </ul>
    <p>Several agencies will participate in the institute; each will focus on one program’s performance management processes. Organizations develop systems at different speeds; the program is designed to accommodate this, with individually designed consultations for each participating agency. The goal is that each agency will develop a culture and practices around performance management. Up to four individuals will consistently participate from each agency, creating a team of performance management and implementation experts within the agency.</p>
  </div>

  <table class="abs schedule">
    <caption>Institute Schedule</caption>
    <thead>
      <tr><th style="width:90px">Format</th><th style="width:173px">Topic</th><th style="width:146px">Date &amp; Time</th><th>Location</th></tr>
    </thead>
    <tbody>
      <tr><td>Consultation 1</td><td>Pre-assessment</td><td class="when">Date<br>8:30am – 12:30pm</td><td class="where">Lakeside Commons<br>Center*</td></tr>
      <tr><td>Session 1</td><td>What’s your impact?</td><td class="when">Date<br>8:30am – 12:30pm</td><td class="where">Lakeside Commons<br>Center*</td></tr>
      <tr><td>Consultation 2</td><td>Individually paced</td><td class="when">Date<br>8:30am – 12:30pm</td><td class="where">Lakeside Commons<br>Center*</td></tr>
      <tr><td>Session 2</td><td>What outcomes can you and<br>should you measure?</td><td class="when">Date<br>8:30am – 12:30pm</td><td class="where">Lakeside Commons<br>Center*</td></tr>
      <tr><td>Session 3</td><td>What processes can you and<br>should you measure?</td><td class="when">Date<br>8:30am – 12:30pm</td><td class="where">Lakeside Commons<br>Center*</td></tr>
      <tr><td>Consultation 3</td><td>Individually paced</td><td class="when">Date<br>8:30am – 12:30pm</td><td class="where">Lakeside Commons<br>Center*</td></tr>
      <tr><td>Consultation 4</td><td>Individually paced</td><td class="when">Date<br>8:30am – 12:30pm</td><td class="where">Lakeside Commons<br>Center*</td></tr>
      <tr><td>Session 4</td><td>What can you and should you<br>do with the results?</td><td class="when">Date<br>8:30am – 12:30pm</td><td class="where">Lakeside Commons<br>Center*</td></tr>
      <tr><td>Consultation 5</td><td>Action planning and<br>post-assessment</td><td class="when">Date<br>8:30am – 12:30pm</td><td class="where">Lakeside Commons<br>Center*</td></tr>
    </tbody>
  </table>
  <p class="abs footnote">* Location tentative and will be confirmed in advance of Session 1.</p>

  <section class="abs deliverables">
    <h2>PROJECT DELIVERABLES</h2>
    <ul>
      <li>A plan that includes performance management systems for one program, and an action plan to develop a system for remaining programs.</li>
      <li>A culture of performance management, including a commitment to high quality program planning, implementation, evaluation and quality improvement, led by a staff team.</li>
    </ul>
  </section>

  <section class="abs cost">
    <h2>INSTITUTE COST</h2>
    <p>The 2017 Institute<br>is offered at<br>$10,000<br>per agency.</p>
  </section>

  <div class="abs copy bio-a">
    <p>Mabel Dorsey joined KTV Advisory Group in 2015 as the co-designer and leader of KTV’s Charting True North performance management institute.</p>
    <p>Mabel is an Associate Professor of Practice at the Halvern School of Social Work at Eastbrook University in Millford. She teaches graduate level social work practice and administration courses, including a course on program development. She is the lead teacher for Social Work Practice with Individuals, Families and Groups and serves on the Curriculum Committee as the Chair of the MSW foundations curriculum. Mabel was awarded the “Excellence in Teaching” faculty award in 2011, 2010, 2008, and 2006.</p>
  </div>

  <div class="abs copy bio-b">
    <p>Mabel co-created and co-led a highly regarded Teaching Toolbox workshop series for faculty. She currently operates an instructional coaching initiative to enhance teaching excellence at the Halvern School. She conducts community trainings on Evidence Based Practice, logic models, groupwork facilitation, professional teambuilding, and adolescent development. Mabel’s experience includes direct social work practice with adolescents in public school and health care settings, and program management experience at the Teen Pregnancy Center at Ridgeview General Hospital.</p>
    <p>KTV Advisory Group Partner Dana Whitlow will assist on the project.</p>
  </div>

  <section class="abs comments">
    <h2>Comments from Prior Participants</h2>
    <p>“The content was extremely relevant and well planned. It felt like it was at "the right level" for agencies that are in a variety of places with their performance management.”</p>
    <p>“What I loved most about the Institute was the combination of one-on-one sessions between our agency and the KTV team paired with the group sessions where we could learn from and collaborate with other agencies.”</p>
    <p>“If your agency is ready to learn how to best measure its data, then absolutely consider the Institute.”</p>
    <p>“If you thought you knew about outcome measurement, you will leave the Institute knowing more and being able to use it!!”</p>
  </section>

  <div class="abs footer-band"></div>
</div>
</body>
</html>
```